2-Page Flyer for the Information Session about the Quiet Venture Pathway

This is a flyer to announce/advertise an evening Information Session about the Quiet Venture Pathway. This Program aims at mindfully rethinking and redesigning work (and life) for people who feel stuck or not entirely satisfied with their work and/or life (please see draft flyer attached for more details). This Program is property of Bright Meadow, a company that uses a combination of Mindfulness, Design, and Entrepreneurship to help people achieve greater happiness (in their work and lives).
Updates

Target Market(s)

People who feel stuck or not entirely satisfied with their work and/or life (please see draft flyer attached for more details)

Font styles to use
Serif
Sans Serif

Colors
ffffff
f37122
33a6d7
acd037

Requirements
Must have
• All of what I will say below is suggestive (I’m not a design expert), and I’m open to divert from it, if it makes sense and feels more interesting.
• I thought initially of a 2-page flyer (please see draft flyer attached). The first page could help people grasp the essence of the event quickly (in 1 or 2 minutes), and then, if they are interested/motivated, they would continue reading through page 2, which has more info about the Program in itself.
• Potential Structure
• Page 1
• . About the Information Session on the Quiet Venture Pathway
• . Visible Date & Time, Contacts, Venue (and other relevant info)
• . About me (the facilitator)
• Page 2
• . About the Quiet Venture Pathway
• I include a Powerpoint draft of the flyer with the content. The design is rudimentary and precarious from an aesthetics/organization point of view, and this is mainly where I need help (and maybe in other aspects too!).
• On the flyer, I would like to include:
• . A photo of myself (I attach 1 picture).
• . 1 or 2 beautiful-nature photos (cropped or full). One may have to do with looking at the sky, dreaming, and imagining a new work and life (2 photos with sky and clouds attached). The other has to do with walking the transformation journey (the photo with the person walking through the forest path).
• . bright meadow logo or logos (there are two slightly different ones, that can be used for different purposes). For the first page, I would like the bright meadow logo that has "bright meadow" written on the bottom, with the saying "Calm, Craft and Enterprise for Joyful Living" beneath. This is the main logo. For the 2nd page, you can choose the logo that adapts better.
• - Where it says the "the way out is in" it would be great to have a similar font to the one I attach (see file "Font_the_way_out_is_in.png" and Torvenscript-qr.ttf
Nice to have
• In terms of colours, I would not divert much from the logo colours (and of course white and black). I would like the flyer to be quite white. Almost like fairy-tale white: the white horse, the white snow, the white of the stars, the white heaven. White could be the base colour. White means peace, tranquillity, calm contentment, a smile.
• And then use the other colours. The green of the mindfulness. The blue of the sky, the dreams. And the orange of the sun, the energy, the fire, the action. And maybe the black for text.
• Where it says the "the way out is in" it would be great to have a similar font to the one I attach (see file "Font_the_way_out_is_in".
• I would like this flyer to be a piece of art, in every possible way. Simple, beautiful, ease, light, peaceful, calm happy. Just like the Quiet Venture Pathway and bright meadow Company that I am creating intends to be. The mission of this Program and Company is to be a designer, a painter (a Picasso) of happier and more fulfilling human lives.
• I am very much looking forward to seeing your proposal(s).

```html
<!DOCTYPE html>
<html lang="en">
<head>
<meta charset="utf-8">
<title>Quiet Venture Pathway – Information Session Flyer</title>
<link href="https://fonts.googleapis.com/css2?family=Oswald:wght@500;600&family=Roboto+Condensed:wght@400;700&family=Caveat:wght@500&display=swap" rel="stylesheet">
<style>
:root{
  --stage:#474747;
  --white:#ffffff;
  --orange:#f37122;
  --blue:#33a6d7;
  --sky:#3d9fdc;
  --sky-deep:#2f8fcf;
  --green:#acd037;
  --ink:#1a1a1a;
  --grey-disc:#b9bcbf;
  --navy-disc:#3f77a8;
}
*{box-sizing:border-box;margin:0;padding:0}
html,body{width:1200px;height:1200px;overflow:hidden;background:var(--stage)}
body{position:relative;font-family:"Roboto Condensed",Arial,sans-serif;color:var(--white)}
.page{position:absolute;overflow:hidden}
.page-front{left:58px;top:258px;width:523px;height:734px;background:var(--white)}
.page-back{left:624px;top:253px;width:526px;height:739px;background:var(--sky)}
.abs{position:absolute}
.heading{font-family:"Oswald",Arial,sans-serif;font-weight:600;text-transform:uppercase;line-height:1}
.pill{position:absolute;font-family:"Oswald",Arial,sans-serif;font-weight:600;color:var(--white);border-radius:12px;padding:0 7px;line-height:20px;height:20px;font-size:15px;text-transform:uppercase;white-space:nowrap}
.pill-orange{background:var(--orange)}
.pill-green{background:var(--green)}
.body-copy{position:absolute;font-size:8.2px;line-height:10.2px;color:var(--white)}
.body-copy b{font-weight:700}
.brand-dot{position:absolute;border-radius:50%;background:var(--blue)}
.brand-name{position:absolute;font-family:"Roboto Condensed",Arial,sans-serif;font-weight:400;color:var(--blue);white-space:nowrap}

/* front page */
.front-brand-dot{left:243px;top:34px;width:38px;height:38px}
.front-brand-name{left:0;width:523px;text-align:center;top:76px;font-size:25px}
.front-tagline{left:0;width:523px;text-align:center;top:113px;font-family:"Oswald",Arial,sans-serif;font-weight:500;font-size:12px;color:var(--ink)}
.program-title{left:0;width:523px;text-align:center;top:146px;font-size:36px}
.t-blue{color:var(--blue)}.t-green{color:var(--green)}.t-orange{color:var(--orange)}
.landscape{left:0;top:200px;width:523px;height:140px;background:linear-gradient(180deg,#ffffff 0%,#e8eef3 30%,#a9b7bf 62%,#7d9196 100%)}
.front-wave{left:0;top:290px;width:523px;height:444px}
.photo-ring{position:absolute;border-radius:50%}
.ring-hills{left:6px;top:268px;width:180px;height:180px;border:6px solid var(--green);background:radial-gradient(circle at 50% 30%,#f2f5f8 0%,#9fc0db 40%,#5d7f5a 70%,#3f5e33 100%)}
.ring-sunrise{left:210px;top:208px;width:168px;height:168px;border:5px solid var(--orange);background:radial-gradient(circle at 55% 45%,#fff2c6 0%,#f6c46a 35%,#d98b3a 70%,#8b5a2b 100%)}
.ring-shore{left:407px;top:232px;width:108px;height:108px;border:5px solid var(--green);background:linear-gradient(180deg,#f4f1ec 0%,#dfe6ea 45%,#b9d3dc 70%,#d9c7a8 100%)}
.event-date{left:197px;top:391px;font-size:24px;color:var(--white);white-space:nowrap}
.time-bar{left:195px;top:418px;width:176px;height:27px}
.time-text{left:210px;top:420px;font-size:20px;color:var(--white);display:flex;align-items:center;gap:7px}
.portrait{left:8px;top:462px;width:174px;height:252px;background:linear-gradient(180deg,#3e8fc9 0%,#5c6f80 35%,#33424f 70%,#27313a 100%)}
.link-bar{left:189px;top:677px;height:14px;line-height:14px;font-size:8.6px;background:var(--green);border-radius:7px;padding:0 6px;white-space:nowrap}
.booking-pill{left:189px;top:699px;height:16px;line-height:16px;padding:0 10px;background:var(--white);color:var(--ink);font-size:10.5px;border-radius:8px 8px 0 0;white-space:nowrap}
.footer{position:absolute;left:0;bottom:0;width:100%;background:var(--orange);color:var(--white);font-size:8.4px;font-weight:700;display:flex;justify-content:center;align-items:center;gap:12px;white-space:nowrap}
.front-footer{height:20px}
.back-footer{height:19px}

/* back page */
.forest{left:0;top:0;width:526px;height:240px;background:linear-gradient(180deg,#2f2b1e 0%,#3b3a25 35%,#1c1a12 62%,#000 80%)}
.back-curve{left:0;top:180px;width:526px;height:120px}
.back-sky{left:0;top:260px;width:526px;height:479px;background:linear-gradient(180deg,#49a7e2 0%,#3d9fdc 45%,#3a98d4 100%)}
.back-brand-dot{left:352px;top:28px;width:38px;height:38px}
.back-brand-name{left:398px;top:24px;font-size:22px;line-height:22px}
.cycle{left:300px;top:285px;width:226px;height:170px}
.list{position:absolute;list-style:none;font-size:9.2px;line-height:12px}
.list li{position:absolute;left:0;padding-left:18px;white-space:nowrap}
.num{position:absolute;left:0;top:0;width:12px;height:12px;border-radius:50%;background:var(--orange);font-size:8px;line-height:12px;text-align:center}
.quote{left:0;width:526px;text-align:center;top:683px;font-family:"Caveat",cursive;font-weight:500;font-size:24px;color:var(--white)}
</style>
</head>
<body>

<!-- FRONT PAGE -->
<section class="page page-front">
  <div class="abs landscape" role="img" aria-label="Soft photo of misty mountain ranges under a pale sky"></div>
  <svg class="abs front-wave" viewBox="0 0 523 444" aria-hidden="true">
    <path d="M0 80 C150 40 330 25 523 30 L523 444 L0 444 Z" fill="var(--sky)"/>
    <path d="M0 80 C150 40 330 25 523 30" fill="none" stroke="var(--white)" stroke-width="7"/>
    <path d="M0 88 C150 48 330 33 523 38" fill="none" stroke="var(--orange)" stroke-width="3"/>
  </svg>

  <div class="brand-dot front-brand-dot"></div>
  <div class="brand-name front-brand-name">bright meadow</div>
  <div class="abs front-tagline">Calm, Craft and Enterprise for Joyful Living</div>
  <h1 class="abs heading program-title"><span class="t-blue">Quiet</span> <span class="t-green">Venture</span> <span class="t-orange">Pathway</span></h1>

  <div class="photo-ring ring-hills" role="img" aria-label="Photo of green hills and valleys under white clouds"></div>
  <div class="photo-ring ring-sunrise" role="img" aria-label="Photo of a woman raising her arms toward the golden sunrise"></div>
  <div class="photo-ring ring-shore" role="img" aria-label="Photo of a person in a hat with open arms facing the sea"></div>

  <div class="abs heading event-date">Thursday 5th September 2019</div>
  <svg class="abs time-bar" viewBox="0 0 176 27" aria-hidden="true"><path d="M6 0 H176 L170 27 H0 Z" fill="var(--green)"/></svg>
  <div class="abs heading time-text">
    <svg width="15" height="15" viewBox="0 0 16 16" aria-hidden="true"><circle cx="8" cy="8" r="8" fill="var(--white)"/><path d="M8 3.5 V8.5 H11.5" stroke="var(--green)" stroke-width="2" fill="none"/></svg>
    19:30 to 21:00
  </div>

  <div class="abs portrait" role="img" aria-label="Portrait photo of the facilitator in a dark jacket and scarf"></div>

  <div class="pill pill-orange" style="left:189px;top:450px">Information Session</div>
  <p class="body-copy" style="left:194px;top:474px;width:320px">The purpose of this Information Session is to give you a real insight into the Quiet Venture Pathway and how it can help you make the most of your professional and personal life.</p>

  <div class="pill pill-green" style="left:189px;top:499px">Who Can Come</div>
  <p class="body-copy" style="left:194px;top:524px;width:320px">The Information Session is <b>FREE</b>. Whether you come on your own, or with friends or family, you'll be warmly welcome. It will take place on Thursday the 5th September 2019, from 19:30 to 21:00, at Kona Cowork. Please get in touch for more info or to book a place.</p>

  <div class="pill pill-orange" style="left:189px;top:561px">Facilitator</div>
  <div class="body-copy" style="left:283px;top:565px;font-size:9.4px;white-space:nowrap">Dr Tomas Ferreira, Visiting Research Fellow, University of Harlow</div>
  <p class="body-copy" style="left:192px;top:584px;width:324px">Tomas joined the University of Harlow (School of Management) as a Lecturer in Entrepreneurship in 2015. He completed his PhD in Entrepreneurship at Kelmor Business School in 2014. His work received the Arden Doctoral Thesis Award from the Society of Management Studies. He began his business career as a production engineer (Volteron), and continued in sales (Arkwell). After his MBA, he worked as a strategy consultant at Douro School of Business. Originally from Portugal, Tomas enjoys designing and launching new ideas, international communities, mindfulness retreats, and musical improvisation. He nurtures a close connection to Willow Hill Mindfulness Centre, where he has practiced and volunteered over 9 months. He has a broad experience of sharing the benefits of mindfulness with others.</p>

  <div class="abs link-bar">More about the facilitator : www.tomasferreira.example/profile</div>
  <div class="abs booking-pill">INFORMATION &amp; BOOKING</div>

  <footer class="footer front-footer">
    <span>hello@brightmeadow.io</span><span>|</span><span>+34 600 555 019 (video call and chat)</span><span>|</span><span>Kona Cowork, C/ Marina 142, Barcelona</span>
  </footer>
</section>

<!-- BACK PAGE -->
<section class="page page-back">
  <div class="abs back-sky"></div>
  <div class="abs forest" role="img" aria-label="Photo of a person walking along a path through a tall pine forest"></div>
  <svg class="abs back-curve" viewBox="0 0 526 120" aria-hidden="true">
    <path d="M0 0 H526 V40 C380 95 150 95 0 45 Z" fill="#000"/>
    <path d="M0 45 C150 95 380 95 526 40" fill="none" stroke="var(--white)" stroke-width="7"/>
    <path d="M0 53 C150 103 380 103 526 48" fill="none" stroke="var(--orange)" stroke-width="6"/>
  </svg>

  <div class="brand-dot back-brand-dot"></div>
  <div class="brand-name back-brand-name">bright<br>meadow</div>

  <div class="pill pill-green" style="left:16px;top:155px;height:24px;line-height:24px;font-size:15px;text-transform:none;padding:0 8px">What is Quiet Venture</div>
  <p class="body-copy" style="left:16px;top:192px;width:494px;font-size:8px;line-height:10.4px">Being mindful means being aware and awake. Entrepreneurship is the creation of a new form of organising. <b>Quiet Venture</b> is then the process of creating or redesigning your work and life with awareness, in a way that is reflective of you, of your passions and values, thus conducing to a greater sense of fulfilment and happiness.</p>

  <div class="pill pill-green" style="left:14px;top:294px;height:22px;line-height:22px">The Program</div>
  <p class="body-copy" style="left:16px;top:326px;width:256px;font-size:9.2px;line-height:12.4px"><b>The Quiet Venture Pathway is a 4-month long transformative</b> journey designed for people who feel stuck or not entirely satisfied with their professional and/or personal life. It will be of benefit for everyone, at any stage.</p>
  <p class="body-copy" style="left:18px;top:387px;width:256px;font-size:9.2px;line-height:12.4px">The Program consists of a 5-hour workshop every month, complemented by 2-hour weekly peer support meetings. It combines mindfulness techniques, design thinking methodology, and entrepreneurship frameworks.</p>

  <svg class="abs cycle" viewBox="0 0 226 170" aria-hidden="true" font-family="Roboto Condensed, Arial, sans-serif" fill="#fff" text-anchor="middle">
    <circle cx="86" cy="40" r="28" fill="var(--green)"/>
    <circle cx="147" cy="90" r="28" fill="var(--navy-disc)"/>
    <circle cx="86" cy="138" r="28" fill="var(--orange)"/>
    <circle cx="30" cy="90" r="28" fill="var(--grey-disc)"/>
    <g font-size="5.4"><text x="86" y="31">Workshop 1</text><text x="147" y="81">Workshop 2</text><text x="86" y="129">Workshop 3</text><text x="30" y="81">Workshop 4</text></g>
    <g font-size="7" font-weight="700"><text x="86" y="40">INSIGHT</text><text x="147" y="90">DESIGN</text><text x="86" y="138">EXECUTE</text><text x="30" y="90">PRESENT</text></g>
    <g font-size="5" font-style="italic"><text x="86" y="48">(5 hours)</text><text x="147" y="98">(5 hours)</text><text x="86" y="146">(5 hours)</text><text x="30" y="98">(5 hours)</text></g>
    <g font-size="6.6"><text x="27" y="43">WPS meetings</text><text x="30" y="140">WPS meetings</text><text x="150" y="140">WPS meetings</text><text x="154" y="30">Weekly Peer Support</text><text x="154" y="38">(WPS) meetings</text><text x="154" y="46">(2hours)</text></g>
    <g fill="none" stroke-width="3" stroke-linecap="round">
      <path d="M48 62 L58 52" stroke="#fff"/><path d="M116 50 L124 58" stroke="var(--green)"/>
      <path d="M128 120 L120 128" stroke="#cfd8e0"/><path d="M54 126 L46 118" stroke="var(--orange)"/>
    </g>
    <path d="M55 47 L61 49 L59 55 Z"/><path d="M121 62 L128 62 L127 55 Z" fill="var(--green)"/>
    <path d="M116 124 L116 131 L123 130 Z" fill="#cfd8e0"/><path d="M41 121 L43 114 L49 117 Z" fill="var(--orange)"/>
  </svg>

  <div class="pill pill-green" style="left:18px;top:469px;height:19px;line-height:19px">Why</div>
  <p class="body-copy" style="left:18px;top:493px;width:222px;font-size:9.2px;line-height:12.4px">Many people are not satisfied with their work or life, but they don't know what to do about it. This Program offers you a safe place to conduct your inner journey with collective support, helping you reflect, design, and (very likely) do something about it. It aims at :</p>
  <ol class="list" style="left:21px;top:576px">
    <li style="top:0"><span class="num">1.</span>Increasing awareness, clarity and confidence</li>
    <li style="top:21px"><span class="num">2.</span>Having a deeper insight on what makes you<br>happier and what you want</li>
    <li style="top:54px"><span class="num">3.</span>Developing a clear design integrating your<br>intended work and life</li>
    <li style="top:87px"><span class="num">4.</span>Start executing this design.</li>
  </ol>

  <div class="pill pill-green" style="left:268px;top:469px;height:19px;line-height:19px">How</div>
  <p class="body-copy" style="left:268px;top:498px;width:248px;font-size:9.2px;line-height:12.4px">This Program differs from existing entrepreneurial programs in many ways:</p>
  <ol class="list" style="left:277px;top:536px">
    <li style="top:0"><span class="num">1.</span>Uses mindfulness and self analysis to look deeply<br>into yourself</li>
    <li style="top:33px"><span class="num">2.</span>Design and execution decisions are based on happiness<br>rather than (only) financials</li>
    <li style="top:66px"><span class="num">3.</span>Holistic and inclusive design process, integrating work<br>and life, and building synergies between your different<br>parts.</li>
  </ol>
  <p class="body-copy" style="left:268px;top:650px;width:248px;font-size:9.2px;line-height:12.4px">The Program format includes lectures, individual work, group sharing, guided activities, experiential exercises, video, audio, handouts and other resources.</p>

  <div class="abs quote">“The way out is in”</div>

  <footer class="footer back-footer">
    <span>hello@brightmeadow.io</span><span>|</span><span>+34 600 555 019 (video call and chat)</span><span>|</span><span>Kona Cowork, C/ Marina 142, Barcelona</span>
  </footer>
</section>

</body>
</html>
```